Shop Image re-design

Hi,

We are a company who operate several convenience stores around Northern Ireland, and are currently trading under a generic name of 'lorn'. We have made a decision to re-brand the stores under the name of "The Quiet Fox", and will start the process by intially trialling the new look by converting our flag ship, and busiest shop to evaluate the results. The stops main focus is on fresh convenience foods - Coffee,sandwichs,fruit,fresh pastries,chilled drinks & juices etc but we also sell the usual items you would expect such as newspapers, magazines, greeting cards, snacks, confectionery etc

This store is situated in a busy hospital and we serve upward of 25,000 customers a week - doctors, nurses, support staff,patients and visitors all of whom come from a wide cross section of society so the design and style of the new rebranding will have to be SPECTACULARY good to win!

The Design we are looking for must be very Professional, stylish, modern, eye catching and yet still display a fun,welcoming and friendly image to our customers.

I have Included some image files of the current look and feel of the branding in the store, these include the outside signage, internal graphics and point of sale material. Its a good image and brand we have at the moment but I want something EXCEPTIONAL that will make us stand out from other retailers, and be memorable to the customers!

Some things to consider...

The main design should be for the outside signage (see image attached for shape, position and general size). The design should not be to cluttered, and the name as mentioned before will be "the quiet fox" but additionally for this store the term "hospital shop" should also be added underneath the main title,but in a much smaller size to the overall name.In other shops we will propably change the term "hospital shop" to "newsagents" where this is more appropriate, but we will redesign this when we come to convert these stores in due course.

I think we should still display some general 'product' images on the outside signage as is currently the case, and if any are included the images should be of a very high resolution and quality, and make you want to eat it!
Although Im suggesting we should keep some sort of images please donot stop your creative processes, if you think something looks good without them...please submit!

The overall 'feel' and style of the outside sign should flow through into the shop with the internal '3d' signage being of a simalar style as well as the point of sale graphics. In submitting for the internal signage please just do so in a 2d format. (see attached images)

The point of sale materal (shelf 'barkers' and a4 posters), that we use around the shop are of a pre-printed coloured card nature that the managers can run through a laser printer to produce store-specific special offers etc. (see attached images)

We are very excited about this re-branding, as we have used artmarketo before to help us design our company stationery etc., with great results! We therefore hope all you talented designers out there can help us make it a reality... so let your creative juices flow we want something very original!

Thanks,

Rupert.

Target Market(s)

As described in the above brief...
It is worth noting that our stores do not operate in 'value focused' enviroment, we are more more concerned with quality of product and speed and quality of service.

Requirements
Must have
• See detailed design brief above.
Nice to have
• It would be good to have a theme that we can transfer across the store onto uniforms, carrier bags, coffee cups and still fits into the overall 'brand' image
Should not have
• Cartoons or childish style designs or graphics!

```html
<!DOCTYPE html>
<html lang="en">
<head>
<meta charset="utf-8">
<title>The Quiet Fox – Hospital Shop Banner</title>
<link href="https://fonts.googleapis.com/css2?family=Open+Sans:wght@400;700&display=swap" rel="stylesheet">
<style>
  :root {
    --page: #ffffff;
    --ink: #1a1a1a;
    --frame: #bdbdbd;
    --yellow-light: #fff200;
    --yellow-mid: #ffe100;
    --yellow-deep: #f6c000;
    --cup-tone-a: #f4f4f4;
    --cup-tone-b: #dedede;
  }
  * { margin: 0; padding: 0; box-sizing: border-box; }
  html, body {
    width: 1200px;
    height: 900px;
    overflow: hidden;
    background: var(--page);
  }
  .canvas {
    position: relative;
    width: 1200px;
    height: 900px;
    background: var(--page);
  }
  .banner {
    position: absolute;
    left: 381px;
    top: 15px;
    width: 438px;
    height: 870px;
    border: 1px solid var(--frame);
    background: var(--page);
    overflow: hidden;
  }
  .banner__bands {
    position: absolute;
    inset: 0;
    width: 100%;
    height: 100%;
  }
  .brand {
    position: absolute;
    left: 0;
    right: 0;
    top: 128px;
    text-align: center;
    font-family: "Open Sans", sans-serif;
    color: var(--ink);
  }
  .brand__name-row {
    display: flex;
    align-items: center;
    justify-content: center;
    gap: 10px;
  }
  .brand__dot {
    width: 22px;
    height: 22px;
    border-radius: 50%;
    background: var(--yellow-mid);
  }
  .brand__name {
    font-weight: 700;
    font-size: 40px;
    letter-spacing: -0.5px;
    line-height: 1;
  }
  .brand__tagline {
    margin-top: 12px;
    font-weight: 400;
    font-size: 13px;
    letter-spacing: 5px;
  }
  .hero-visual {
    position: absolute;
    left: 20px;
    top: 285px;
    width: 220px;
    height: 230px;
    border-radius: 4px;
    background: linear-gradient(160deg, var(--cup-tone-a), var(--cup-tone-b));
  }
  .slogan {
    position: absolute;
    font-family: "Open Sans", sans-serif;
    font-weight: 700;
    font-size: 20px;
    line-height: 1;
    color: var(--ink);
    white-space: nowrap;
    transform: translate(-50%, -50%) rotate(-29deg);
  }
  .slogan--headline { left: 262px; top: 712px; }
  .slogan--hours { left: 252px; top: 788px; }
</style>
</head>
<body>
  <main class="canvas">
    <section class="banner">
      <svg class="banner__bands" viewBox="0 0 256 509" preserveAspectRatio="none" aria-hidden="true">
        <defs>
          <linearGradient id="band-upper" x1="1" y1="0" x2="0" y2="1">
            <stop offset="0" stop-color="#fff200"/>
            <stop offset="1" stop-color="#ffd800"/>
          </linearGradient>
          <linearGradient id="band-lower" x1="1" y1="0" x2="0" y2="1">
            <stop offset="0" stop-color="#ffe100"/>
            <stop offset="1" stop-color="#f6c000"/>
          </linearGradient>
        </defs>
        <polygon class="band band--upper" points="256,195 256,314 0,482" fill="url(#band-upper)"/>
        <polygon class="band band--lower" points="256,332 256,509 0,509 0,497" fill="url(#band-lower)"/>
      </svg>

      <header class="brand">
        <div class="brand__name-row">
          <span class="brand__dot"></span>
          <span class="brand__name">The Quiet Fox</span>
        </div>
        <div class="brand__tagline">HOSPITAL SHOP</div>
      </header>

      <div class="hero-visual" role="img" aria-label="Line illustration of a steaming coffee cup"></div>

      <p class="slogan slogan--headline">Sip, Munch and Zip</p>
      <p class="slogan slogan--hours">8am to 9pm, 7 days a week</p>
    </section>
  </main>
</body>
</html>
```